Brimovex business card

Based on company logo and website given , to design a business card temple. Slogan "Gentle care for every companion"
Color style please refer to our website

```html
<!DOCTYPE html>
<html lang="en">
<head>
<meta charset="utf-8">
<title>Brimovex business card</title>
<link href="https://fonts.googleapis.com/css2?family=Open+Sans:ital,wght@0,400;0,700;1,400&display=swap" rel="stylesheet">
<style>
  :root {
    --page-bg: #2b2b2b;
    --card-bg: #1b1b1c;
    --accent: #bdb629;
    --silver: #a9a9ab;
    --text: #f1f1f1;
  }
  * { box-sizing: border-box; margin: 0; padding: 0; }
  html, body { width: 1200px; height: 900px; overflow: hidden; }
  body {
    background: var(--page-bg);
    font-family: "Open Sans", Arial, sans-serif;
    position: relative;
  }
  .card {
    position: absolute;
    left: 250px;
    width: 700px;
    height: 400px;
    background: var(--card-bg);
    box-shadow: 0 10px 30px rgba(0,0,0,0.45);
    color: var(--text);
  }
  .card--front { top: 40px; }
  .card--back { top: 460px; }

  .wordmark {
    position: absolute;
    display: flex;
    align-items: center;
    gap: 12px;
    font-weight: 700;
    letter-spacing: -1px;
    line-height: 1;
  }
  .wordmark__dot { width: 14px; height: 14px; border-radius: 50%; }

  .card--front .wordmark { left: 120px; top: 50px; font-size: 56px; color: var(--accent); }
  .card--front .wordmark__dot { background: var(--accent); }

  .divider {
    position: absolute;
    left: 60px; right: 60px; top: 205px;
    height: 2px;
    background: var(--accent);
  }

  .contact-list {
    position: absolute;
    left: 60px; top: 232px;
    list-style: none;
    font-size: 17px;
    line-height: 28px;
  }
  .contact-list li { display: flex; align-items: center; gap: 10px; }
  .contact-list svg { width: 14px; height: 14px; fill: var(--accent); flex: none; }

  .person {
    position: absolute;
    right: 60px; top: 132px;
    text-align: right;
    line-height: 1.3;
  }
  .person__name {
    font-size: 24px; font-weight: 700; color: var(--accent);
    letter-spacing: 0.5px; text-transform: uppercase;
  }
  .person__role { font-size: 18px; font-style: italic; }

  .address {
    position: absolute;
    right: 60px; top: 232px;
    text-align: right;
    font-size: 18px;
    line-height: 28px;
    font-style: normal;
  }

  .card--back .wordmark {
    left: 50%; top: 130px; transform: translateX(-50%);
    font-size: 84px; color: var(--silver);
  }
  .card--back .wordmark__dot { background: var(--silver); width: 18px; height: 18px; }
  .slogan {
    position: absolute;
    left: 0; right: 0; top: 262px;
    text-align: center;
    font-size: 20px;
    font-style: italic;
    color: var(--text);
  }
</style>
</head>
<body>
  <section class="card card--front" aria-label="Card front">
    <div class="wordmark"><span class="wordmark__name">Brimovex</span><span class="wordmark__dot"></span></div>

    <div class="person">
      <p class="person__name">Dana Kerrow</p>
      <p class="person__role">President</p>
    </div>

    <div class="divider"></div>

    <ul class="contact-list">
      <li>
        <svg viewBox="0 0 24 24" aria-hidden="true"><path d="M6.6 10.8a15 15 0 0 0 6.6 6.6l2.2-2.2a1 1 0 0 1 1-.25 11.4 11.4 0 0 0 3.6.57 1 1 0 0 1 1 1V20a1 1 0 0 1-1 1A17 17 0 0 1 3 4a1 1 0 0 1 1-1h3.5a1 1 0 0 1 1 1c0 1.25.2 2.45.57 3.57a1 1 0 0 1-.25 1z"/></svg>
        <span>555-014-2290</span>
      </li>
      <li>
        <svg viewBox="0 0 24 24" aria-hidden="true"><path d="M2 5h20l-10 8z M2 7.5l10 8 10-8V19H2z"/></svg>
        <span>dkerrow@brimovex.com</span>
      </li>
      <li>
        <svg viewBox="0 0 24 24" aria-hidden="true"><circle cx="12" cy="12" r="10"/></svg>
        <span>www.brimovex.com</span>
      </li>
    </ul>

    <address class="address">1840 Harbor Crest Way<br>Marlow Bay CA 90412</address>
  </section>

  <section class="card card--back" aria-label="Card back">
    <div class="wordmark"><span class="wordmark__name">Brimovex</span><span class="wordmark__dot"></span></div>
    <p class="slogan">Gentle care for every companion</p>
  </section>
</body>
</html>
```